Brightwater Facility Partners Business card

We wish to have a professional Business card to present to large Corporate CEO's ASAP.

Our web site helps explain our business www.brightwaterfp.org

Brightwater Facility Partners was established after we discovered how difficult it is to organise outsourced services while heading up a business or company.

We act as a facilitator for businesses who don't have the desire, expertise or recourses to manage their own systems and meet all their requirements.

We provide an all in one facility management solution for all types of businesses. We manage schedules, contractors and costs on behalf of businesses and their needs and wants.

Having an extensive network ensures we are able to connect businesses with the right service providers.

Target Market(s)

Company CEO

Industry/Entity Type

Business

Font styles to use
Sans Serif

Colors
33a6d7
f9fdfe
0355a3

Requirements
Must have
• professional design
Nice to have
• colours to match logo

```html
<!DOCTYPE html>
<html lang="en">
<head>
<meta charset="utf-8">
<title>Brightwater Facility Partners – Business Card</title>
<link rel="stylesheet" href="https://fonts.googleapis.com/css2?family=Open+Sans:wght@400;600&family=Roboto+Condensed:wght@400;700&display=swap">
<style>
  :root {
    --brand-blue: #0a72bd;
    --brand-deep: #0355a3;
    --brand-sky: #33a6d7;
    --paper: #f9fdfe;
    --backdrop: #c9c9cb;
    --pill-light: #ffffff;
    --pill-shade: #cfd3d8;
    --ink-dark: #1c1c1c;
  }
  * { margin: 0; padding: 0; box-sizing: border-box; }
  html, body {
    width: 1200px; height: 883px; overflow: hidden;
    background: radial-gradient(ellipse at 50% 40%, #dedee0 0%, var(--backdrop) 100%);
  }
  .business-card {
    position: absolute; left: 110px; top: 161px;
    width: 980px; height: 560px;
    background: var(--paper);
    overflow: hidden;
    box-shadow: 0 14px 34px rgba(0,0,0,.22);
  }
  .card-base { position: absolute; inset: 0; }
  .brand {
    position: absolute; left: 42px; top: 46px;
    display: flex; align-items: center; gap: 16px;
  }
  .brand-dot {
    width: 44px; height: 44px; border-radius: 50%;
    background: var(--brand-sky);
  }
  .brand-name {
    font-family: "Roboto Condensed", sans-serif;
    font-weight: 700; font-size: 36px; letter-spacing: .5px;
    color: var(--brand-deep); text-transform: uppercase;
  }
  .service-list {
    position: absolute; left: 30px; top: 214px; width: 300px;
    list-style: none;
  }
  .service-list li {
    font-family: "Roboto Condensed", sans-serif;
    font-size: 19px; color: var(--paper);
    text-align: right; text-transform: uppercase;
    padding: 8px 0 5px;
    border-top: 2px solid var(--paper);
    line-height: 22px;
  }
  .contact-name {
    position: absolute; left: 560px; top: 176px;
    font-family: "Open Sans", sans-serif; font-size: 30px;
    color: var(--paper);
  }
  .contact-row {
    position: absolute; left: 500px; width: 480px; height: 50px;
    display: flex; align-items: center;
  }
  .contact-icon { width: 40px; height: 40px; flex: none; }
  .contact-pill {
    margin-left: 20px; flex: 1; height: 50px;
    border-radius: 25px 0 0 25px;
    background: linear-gradient(90deg, var(--pill-light) 35%, var(--pill-shade) 100%);
    border-bottom: 4px solid var(--brand-deep);
    display: flex; align-items: center; padding-left: 24px;
    font-family: "Open Sans", sans-serif; font-weight: 600;
    font-size: 24px; color: var(--brand-deep);
  }
  .row-phone { top: 232px; }
  .row-email { top: 305px; }
  .row-web { top: 378px; }
</style>
</head>
<body>
  <div class="business-card">
    <svg class="card-base" width="980" height="560" viewBox="0 0 980 560" aria-hidden="true">
      <path d="M0 196 H480 C560 196 580 140 660 140 H900 Q980 140 980 220 V560 H0 Z" fill="var(--brand-blue)"/>
    </svg>

    <div class="brand">
      <span class="brand-dot"></span>
      <span class="brand-name">Brightwater Facility Partners</span>
    </div>

    <ul class="service-list">
      <li>Cleaning</li>
      <li>Waste Management</li>
      <li>Security and Electrical</li>
      <li>Fire Safety</li>
      <li>Building Maintenance</li>
      <li>Plumbing</li>
      <li>Pest Control</li>
      <li>Landscape Maintenance</li>
    </ul>

    <div class="contact-name">Daniel Hartley</div>

    <div class="contact-row row-phone">
      <svg class="contact-icon" viewBox="0 0 40 40" aria-label="Phone">
        <circle cx="20" cy="20" r="17" fill="none" stroke="var(--paper)" stroke-width="1.5"/>
        <path d="M14 12 l4 0 l1.5 5 l-2.5 1.5 a10 10 0 0 0 5 5 l1.5 -2.5 l5 1.5 l0 4 a2 2 0 0 1 -2 2 a16 16 0 0 1 -14.5 -14.5 a2 2 0 0 1 2 -2z" fill="none" stroke="var(--paper)" stroke-width="1.5" stroke-linejoin="round"/>
      </svg>
      <div class="contact-pill">0400 218 736</div>
    </div>

    <div class="contact-row row-email">
      <svg class="contact-icon" viewBox="0 0 40 40" aria-label="Email">
        <circle cx="20" cy="20" r="17" fill="none" stroke="var(--paper)" stroke-width="1.5"/>
        <rect x="11" y="14" width="18" height="12" rx="1" fill="none" stroke="var(--paper)" stroke-width="1.5"/>
        <path d="M11 14 l9 7 l9 -7" fill="none" stroke="var(--paper)" stroke-width="1.5"/>
      </svg>
      <div class="contact-pill">daniel@brightwaterfp.org</div>
    </div>

    <div class="contact-row row-web">
      <svg class="contact-icon" viewBox="0 0 40 40" aria-label="Website">
        <circle cx="20" cy="20" r="17" fill="none" stroke="var(--paper)" stroke-width="1.5"/>
        <rect x="11" y="12" width="18" height="16" rx="1" fill="none" stroke="var(--paper)" stroke-width="1.5"/>
        <line x1="11" y1="16" x2="29" y2="16" stroke="var(--paper)" stroke-width="1.5"/>
        <line x1="14" y1="20" x2="26" y2="20" stroke="var(--paper)" stroke-width="1.2"/>
        <line x1="14" y1="24" x2="22" y2="24" stroke="var(--paper)" stroke-width="1.2"/>
      </svg>
      <div class="contact-pill">www.brightwaterfp.org</div>
    </div>
  </div>
</body>
</html>
```